PowerPoint Design

We require a sample PowerPoint design so we can pitch PPT design services to a client.

The designs do NOT need to be done in PowerPoint, but should reflect designs that *could* be created in PPT format.

We require 3 slides as part of this project:

1. A slide containing the statistical chart based on data in Figure 3.3 at http://www7.dovrimark.org/survey-releves/2006/tb-qr/ab-cd/index.cfm?LANG=ENG&VIEW=C&format=flash&PRCODE=01&TOPIC_ID=2
-> note, don't just copy and paste the existing graph - come up with something innovative and eye catching

2. Inspirational slide to motivate employees. Zorvex "inspirational quote" and select a quote you think is appropriate. Imagery should generate enthusiasm/optimism.

3. A slide of your own choosing.
Updates

Project Deadline Extended
Reason: One of the team reviewing the designs is away from office. We've decided to give other designers a chance to submit ideas. Final decision will be made on December 5th, 2011.

Target Market(s)

Business professionals

Industry/Entity Type

Zorvex

Requirements
Must have
• Must have 3 slides.

```html
<!DOCTYPE html>
<html lang="en">
<head>
<meta charset="utf-8">
<title>Ships in Harbour</title>
<link rel="stylesheet" href="https://fonts.googleapis.com/css2?family=Carlito&family=Comic+Neue:wght@700&display=swap">
<style>
  :root {
    --slide-teal: #1b97bb;
    --band-black: #000000;
    --quote-white: #ffffff;
    --card-white: #f7f7f7;
    --card-edge: #d9d9d9;
    --sea-deep: #0b2f8a;
    --sea-mid: #1a49a8;
    --caption-ink: #111111;
  }
  html, body {
    margin: 0;
    padding: 0;
    width: 1200px;
    height: 900px;
    overflow: hidden;
  }
  .slide {
    position: relative;
    width: 1200px;
    height: 900px;
    background: var(--slide-teal);
    overflow: hidden;
    font-family: "Carlito", "Calibri", sans-serif;
  }
  .quote-band {
    position: absolute;
    left: 0;
    background: var(--band-black);
    color: var(--quote-white);
    font-size: 45px;
    line-height: 54px;
    padding: 8px 0 0 35px;
    box-sizing: border-box;
    margin: 0;
    font-weight: 400;
  }
  .quote-band--first { top: 185px; width: 588px; height: 132px; }
  .quote-band--second { top: 447px; width: 558px; height: 140px; padding-top: 13px; }

  .snapshot {
    position: absolute;
    left: 585px;
    top: 123px;
    width: 580px;
    height: 505px;
    box-sizing: border-box;
    background: var(--card-white);
    border: 1px solid var(--card-edge);
    box-shadow: 2px 3px 6px rgba(0,0,0,0.35);
  }
  .snapshot--back { transform: translate(10px, 12px) rotate(2.4deg); }
  .snapshot--front { transform: rotate(3.4deg); }
  .snapshot__photo {
    position: absolute;
    left: 18px;
    top: 40px;
    width: 544px;
    height: 405px;
    background: radial-gradient(ellipse at 30% 60%, var(--sea-mid), var(--sea-deep) 80%);
  }
  .snapshot__caption {
    position: absolute;
    right: 48px;
    bottom: 22px;
    margin: 0;
    font-family: "Comic Neue", "Comic Sans MS", cursive;
    font-weight: 700;
    font-size: 24px;
    color: var(--caption-ink);
    letter-spacing: 0.5px;
  }
</style>
</head>
<body>
  <main class="slide">
    <h1 class="quote-band quote-band--first">SHIPS IN HARBOUR<br>ARE SAFE,</h1>
    <p class="quote-band quote-band--second">BUT THAT’S NOT WHAT<br>SHIPS ARE BUILT FOR!</p>

    <div class="snapshot snapshot--back" aria-hidden="true"></div>
    <figure class="snapshot snapshot--front" style="margin:0">
      <div class="snapshot__photo" role="img" aria-label="Photo of a white sailing catamaran on a deep blue open sea"></div>
      <figcaption class="snapshot__caption">Adventure 2011</figcaption>
    </figure>
  </main>
</body>
</html>
```